Baby Adoption Announcement

I'm looking for a simple, understated and modern baby adoption announcement.

The baby is a boy, but I don't want anything that is blue or particularly boyish. No storks, baby baskets, rattles, or traditional baby announcement designs. No cutesy or busy designs.

Should measure 5.25 x 8.25 inches to fit in an A9 envelope.

Simple graphics MIGHT include birds, grasses, trees, rivers. I'm open to other ideas. Text can be a single color or multi colored. Graphics are not mandatory.

Since this is text heavy, I'd like the designer to be REALLY GOOD at choosing fonts and typesetting.

Text should read:

Memory answers us bright on your face—
Impossibly, we spoke and were silent
Together before all of this. (in italics)

Cornelius Tobias Pelter Quist
Born on March 16, 2012 in Boston, MA
and entrusted to us by his birthmother, Gwenda.

Named Cornelius, which means God is with us, after Gwenda’s grandfather &
Tobias, after Toby and St. Tobias of Karvel

• Should measure 5.25 x 8.25 inches to fit in A9 envelope.

• The baby is a boy, but I don't want anything that is blue or particularly boyish. No storks, baby baskets, rattles, or traditional baby announcement designs. Nothing cutesy or busy.

```html
<!DOCTYPE html>
<html lang="en">
<head>
<meta charset="utf-8">
<title>Adoption Announcement – Cornelius Tobias Pelter Quist</title>
<link rel="stylesheet" href="https://fonts.googleapis.com/css2?family=Great+Vibes&family=Cinzel:wght@400;500&family=EB+Garamond:wght@400;500&display=swap">
<style>
  :root {
    --paper: #ffffff;
    --brown: #6e3b14;
    --olive: #9a8a57;
    --navy: #3f4a5f;
    --rule: #d4d4d4;
    --stamp: #c9c9c9;
  }
  * { margin: 0; padding: 0; box-sizing: border-box; }
  html, body {
    width: 1200px;
    height: 800px;
    overflow: hidden;
    background: var(--paper);
  }
  .card {
    position: relative;
    width: 1200px;
    height: 800px;
    background: var(--paper);
  }
  .card__frame {
    position: absolute;
    inset: 0;
  }
  .stamp-label {
    position: absolute;
    left: 155px;
    top: 400px;
    transform: translate(-50%, -50%) rotate(90deg);
    font-family: "EB Garamond", serif;
    font-size: 24px;
    letter-spacing: 4px;
    font-variant: small-caps;
    color: var(--stamp);
  }
  .message {
    position: absolute;
    left: 300px;
    right: 40px;
    top: 0;
    text-align: center;
    color: var(--brown);
    font-family: "EB Garamond", serif;
  }
  .message__greeting {
    position: absolute;
    left: 0; right: 0;
    top: 112px;
    font-family: "Great Vibes", cursive;
    font-size: 50px;
    font-weight: 400;
    line-height: 1;
  }
  .message__name {
    position: absolute;
    left: 0; right: 0;
    top: 255px;
    font-family: "Cinzel", serif;
    font-size: 34px;
    font-weight: 500;
    letter-spacing: 1px;
    line-height: 1;
  }
  .message__name .initial { font-size: 42px; }
  .message__birth,
  .message__naming {
    position: absolute;
    left: 0; right: 0;
    font-size: 24px;
    line-height: 44px;
  }
  .message__birth { top: 350px; }
  .message__naming { top: 488px; line-height: 38px; }
  .birthmother {
    font-family: "Great Vibes", cursive;
    font-size: 34px;
    color: var(--olive);
  }
  .meaning {
    font-variant: small-caps;
    font-size: 27px;
    letter-spacing: 0.5px;
    color: var(--olive);
  }
  .caps { font-variant: small-caps; font-size: 27px; letter-spacing: 0.5px; }
</style>
</head>
<body>
  <main class="card">
    <svg class="card__frame" width="1200" height="800" viewBox="0 0 1200 800" aria-hidden="true">
      <rect x="10" y="10" width="1180" height="780" rx="30" fill="none" stroke="var(--olive)" stroke-width="8"/>
      <rect x="22" y="22" width="1156" height="756" rx="26" fill="none" stroke="var(--brown)" stroke-width="7"/>
      <rect x="39" y="39" width="1122" height="722" rx="26" fill="none" stroke="var(--navy)" stroke-width="8"/>
      <line x1="300" y1="44" x2="300" y2="756" stroke="var(--rule)" stroke-width="2"/>
    </svg>

    <div class="stamp-label">Stamp</div>

    <section class="message">
      <h1 class="message__greeting">We Welcome with Joy</h1>
      <h2 class="message__name"><span class="initial">C</span>ORNELIUS <span class="initial">T</span>OBIAS <span class="initial">P</span>ELTER <span class="initial">Q</span>UIST</h2>
      <p class="message__birth">
        Born on March 16, 2012 in Boston, MA<br>
        and entrusted to us by his birthmother, <span class="birthmother">Gwenda.</span>
      </p>
      <p class="message__naming">
        Named <span class="caps">Cornelius</span>, which means <span class="meaning">God is with us</span><br>
        after Gwenda’s grandfather &amp;<br>
        <span class="caps">Tobias</span>, after Toby and <span class="caps">St. Tobias of Karvel</span>
      </p>
    </section>
  </main>
</body>
</html>
```